Every Shelf Neatly Sorted or ESN Organized needs a business card design. ESN Organized is a professi

We need a business card design that is clean, sharp and conveys a sense of organization. I already have a logo.

Reason: I am still providing feedback and need more time.

Target Market(s)

Families (specifically mothers), small business owners, parents, seniors

Industry/Entity Type

Business

Contact Information for Business Card

My website is www.esnsortedhome.example and my ShareCircle page is www.sharecircle.example/everyshelfneatlysorted. The phone number is 555-418-2706 and I want to be listed as Marla V. Osgood, Owner

Requirements
Must have
• My logo.

```html
<!DOCTYPE html>
<html lang="en">
<head>
<meta charset="utf-8">
<title>Every Shelf Neatly Sorted – Business Card</title>
<link rel="stylesheet" href="https://fonts.googleapis.com/css2?family=Karla:wght@400&family=Lora:wght@400&display=swap">
<style>
  :root {
    --stage: #ece9e4;
    --card: #ffffff;
    --brand-blue: #0b74b8;
    --ink: #1c1c1c;
    --shadow: rgba(0, 0, 0, 0.18);
  }
  * { margin: 0; padding: 0; box-sizing: border-box; }
  html, body {
    width: 1200px;
    height: 1200px;
    overflow: hidden;
    background: var(--stage);
  }
  .stage {
    width: 1200px;
    height: 1200px;
    display: flex;
    align-items: center;
    justify-content: center;
  }
  .business-card {
    position: relative;
    width: 1050px;
    height: 600px;
    background: var(--card);
    box-shadow: 0 10px 30px var(--shadow);
    font-family: "Karla", Arial, sans-serif;
    color: var(--ink);
  }
  .accent-band {
    position: absolute;
    top: 0;
    right: 0;
    width: 130px;
    height: 100%;
    background: var(--brand-blue);
  }
  .brand-name {
    position: absolute;
    left: 80px;
    top: 96px;
    display: flex;
    align-items: center;
    gap: 20px;
  }
  .brand-mark {
    width: 52px;
    height: 52px;
    border-radius: 50%;
    background: var(--brand-blue);
    flex: none;
  }
  .brand-wordmark {
    font-family: "Karla", Arial, sans-serif;
    font-weight: 400;
    font-size: 44px;
    letter-spacing: 1px;
    color: var(--brand-blue);
    white-space: nowrap;
  }
  .owner-name {
    position: absolute;
    left: 88px;
    top: 282px;
    font-family: "Lora", Georgia, serif;
    font-weight: 400;
    font-size: 40px;
    color: var(--brand-blue);
  }
  .owner-title {
    position: absolute;
    left: 90px;
    top: 340px;
    font-size: 22px;
    letter-spacing: 0.5px;
  }
  .contact-list {
    position: absolute;
    left: 92px;
    top: 392px;
    list-style: none;
    display: flex;
    flex-direction: column;
    gap: 14px;
  }
  .contact-item {
    display: flex;
    align-items: center;
    gap: 10px;
    font-size: 27px;
    letter-spacing: 0.3px;
    white-space: nowrap;
  }
  .contact-icon {
    width: 20px;
    height: 20px;
    flex: none;
  }
  .social-square {
    width: 18px;
    height: 18px;
    margin: 0 1px;
    background: var(--brand-blue);
    flex: none;
  }
</style>
</head>
<body>
<main class="stage">
  <section class="business-card" aria-label="Every Shelf Neatly Sorted business card">
    <div class="brand-name">
      <span class="brand-mark" aria-hidden="true"></span>
      <span class="brand-wordmark">Every Shelf Neatly Sorted</span>
    </div>

    <h1 class="owner-name">Marla V. Osgood</h1>
    <p class="owner-title">Owner</p>

    <ul class="contact-list">
      <li class="contact-item">
        <svg class="contact-icon" viewBox="0 0 24 24" aria-hidden="true">
          <path d="M6.6 3.5 9.3 7c.4.5.3 1.2-.1 1.6L7.8 10c1.2 2.5 3.3 4.6 5.8 5.8l1.4-1.4c.4-.4 1.1-.5 1.6-.1l3.5 2.7c.5.4.6 1.2.1 1.7l-1.8 1.9c-.7.7-1.8.9-2.7.5C9.8 18.9 5.1 14.2 2.9 8.3c-.4-.9-.2-2 .5-2.7l1.9-1.8c.4-.5 1.2-.4 1.3-.3z" fill="var(--brand-blue)"/>
        </svg>
        <span>555-418-2706</span>
      </li>
      <li class="contact-item">
        <svg class="contact-icon" viewBox="0 0 24 24" aria-hidden="true" fill="none" stroke="var(--brand-blue)" stroke-width="1.6">
          <circle cx="12" cy="12" r="9.5"/>
          <ellipse cx="12" cy="12" rx="4.2" ry="9.5"/>
          <line x1="2.5" y1="12" x2="21.5" y2="12"/>
          <line x1="4" y1="7" x2="20" y2="7"/>
          <line x1="4" y1="17" x2="20" y2="17"/>
        </svg>
        <span>www.esnsortedhome.example</span>
      </li>
      <li class="contact-item">
        <span class="social-square" aria-hidden="true"></span>
        <span>www.sharecircle.example/everyshelfneatlysorted</span>
      </li>
    </ul>

    <div class="accent-band" aria-hidden="true"></div>
  </section>
</main>
</body>
</html>
```